Tralvo GmbH banner ad

Banner ad for Facebook Our company name (logo) Title: Transporter and bus rental Text: Without deposit, super prices

Target Market(s)

Rental

Requirements
Must have
• LOGO from us, Evt. A pair of transporters in the picture

```html
<!DOCTYPE html>
<html lang="de">
<head>
<meta charset="utf-8">
<title>Tralvo GmbH – Transporter and Bus Rental</title>
<link rel="stylesheet" href="https://fonts.googleapis.com/css2?family=Tinos&family=Arimo:wght@400;700&family=Oswald:wght@600;700&display=swap">
<style>
  :root {
    --navy: #0b0a7a;
    --steel: #7f97b0;
    --pill-grey: #a7abb3;
    --ink: #2b2b33;
    --white: #ffffff;
    --vehicle-light: #eef0f3;
    --vehicle-mid: #b9bec6;
  }
  html, body {
    margin: 0;
    width: 1200px;
    height: 572px;
    overflow: hidden;
    background: var(--white);
  }
  .banner {
    position: absolute;
    left: 134px;
    top: 112px;
    width: 927px;
    height: 343px;
    display: block;
    box-shadow: 0 4px 14px rgba(0, 0, 0, 0.25);
  }
  .brand-name { font-family: "Arimo", sans-serif; font-weight: 700; }
  .title-main { font-family: "Tinos", serif; }
  .title-sub { font-family: "Arimo", sans-serif; }
  .badge-text, .offer-text { font-family: "Oswald", sans-serif; font-weight: 700; }
</style>
</head>
<body>
<svg class="banner" viewBox="0 0 850 314" xmlns="http://www.w3.org/2000/svg" aria-label="Tralvo GmbH: Transporter and bus rental, ohne Kaution, Superpreise">
  <defs>
    <linearGradient id="vehicle-tone" x1="0" y1="0" x2="1" y2="1">
      <stop offset="0" stop-color="var(--vehicle-light)"/>
      <stop offset="1" stop-color="var(--vehicle-mid)"/>
    </linearGradient>
  </defs>

  <!-- background -->
  <rect class="canvas-fill" width="850" height="314" fill="var(--white)"/>

  <!-- left navy field and diagonal stripe -->
  <polygon class="field-left" points="0,0 334,0 184,314 0,314" fill="var(--navy)"/>
  <polygon class="stripe-left" points="368,0 424,0 276,314 218,314" fill="var(--steel)"/>

  <!-- bottom-right corner accent -->
  <polygon class="stripe-corner" points="850,146 850,154 728,314 720,314" fill="var(--steel)"/>
  <polygon class="field-corner" points="850,164 850,314 737,314" fill="var(--navy)"/>

  <!-- brand -->
  <g class="brand">
    <rect class="brand-mark" x="32" y="21" width="30" height="30" fill="none" stroke="var(--white)" stroke-width="2.5"/>
    <text class="brand-name" x="70" y="44" font-size="19" fill="var(--white)">TRALVO</text>
  </g>

  <!-- coach photo area -->
  <rect class="vehicle-photo" role="img" aria-label="Photo of a white touring coach, seen from the front left"
        x="22" y="62" width="356" height="238" rx="26" fill="url(#vehicle-tone)"/>

  <!-- headline -->
  <text class="title-main" x="430" y="86" font-size="50" textLength="388" lengthAdjust="spacingAndGlyphs" fill="var(--navy)">TRANSPORTER</text>
  <text class="title-sub" x="428" y="128" font-size="44" textLength="396" lengthAdjust="spacingAndGlyphs" fill="var(--steel)">AND BUS RENTAL</text>

  <!-- offer pill -->
  <path class="offer-pill" d="M552,199 H822 L822,242 H552 A21.5,21.5 0 0 1 552,199 Z" fill="var(--pill-grey)"/>
  <text class="offer-text" x="547" y="235" font-size="36" textLength="228" lengthAdjust="spacingAndGlyphs" fill="var(--navy)">SUPERPREISE</text>

  <!-- deposit badge -->
  <g class="badge">
    <circle cx="469" cy="221" r="54" fill="var(--steel)"/>
    <circle cx="469" cy="221" r="50" fill="var(--white)"/>
    <circle cx="469" cy="221" r="44" fill="none" stroke="var(--navy)" stroke-width="5"/>
    <text class="badge-text" x="469" y="214" font-size="17" text-anchor="middle" fill="var(--steel)">OHNE</text>
    <text class="badge-text" x="469" y="237" font-size="20" text-anchor="middle" fill="var(--ink)">KAUTION</text>
  </g>
</svg>
</body>
</html>
```